we need a homepage for a marketplace

We manage all projects using our ground-breaking platform Kelvrim Hub. You get access to 150+ partners in 70 countries, security, cost efficiency, technical skills, speed, 100% visibility and accountability.Kelvrim aims to help clients realize the full potential of their investments, provide a competitive price, establish the business need as a competitive advantage, and provide a strategic business asset that can facilitate growth.
Target Market(s)
Freelancers
Industry/Entity Type
Business Software
Number of Pages Required
1 page
Requirements
Must have
- Credentials -http://qabdel.example/freelancer/public
- Front :
- Client:
- Email id - tomasp@lurvantsystems.example
- Password - 908172
- Partner:
- Email id - dorian@lurvantsystems.example
- Password - 908172
- Project Manager:
- Email id - mirela@lurvantsystems.example
- Password - 908172
Nice to have
- It will be nice to have a creative design, and a outside the box look/feel

```html
<!DOCTYPE html>
<html lang="en">
<head>
<meta charset="utf-8">
<title>Kelvrim Hub – Marketplace</title>
<link rel="stylesheet" href="https://fonts.googleapis.com/css2?family=Lato:wght@400;700&display=swap">
<style>
:root{
  --accent-bar:#a77fcf;
  --hero:#2f67a6;
  --hero-dark:#24548c;
  --login:#9ef01a;
  --link:#5aa2ea;
  --pill:#a8cdf5;
  --pill-line:#8fbff0;
  --table:#a9cdf6;
  --grey:#e9eaec;
  --grey-mid:#d9dadc;
  --grey-text:#a7aaaf;
  --text:#7d8187;
  --white:#ffffff;
  --card:#25588f;
}
*{box-sizing:border-box;margin:0;padding:0}
html,body{width:1200px;height:2483px;overflow:hidden;background:var(--white);font-family:'Lato',sans-serif;color:var(--text)}
.canvas{position:relative;width:1200px;height:2483px}
.abs{position:absolute}
.top-bar{left:0;top:0;width:1200px;height:7px;background:var(--accent-bar)}
.nav-link{top:26px;font-size:15px;color:var(--grey-text)}
.login{left:1018px;top:22px;width:99px;height:28px;border-radius:14px;background:var(--login);color:var(--white);font-weight:700;font-size:15px;text-align:center;line-height:28px}
.hero{left:0;top:65px;width:1200px;height:430px;background:linear-gradient(180deg,#3470b0,var(--hero-dark))}
.logo{left:68px;top:61px;width:192px;height:90px;background:var(--white);display:flex;align-items:center;justify-content:center;gap:8px;z-index:2}
.logo-mark{width:22px;height:22px;background:var(--hero)}
.logo-name{font-size:30px;font-weight:400;color:#25466f}
.hero-visual{left:409px;top:127px;width:460px;height:370px;border-radius:10px;background:linear-gradient(180deg,#e8eef5,#b9c3cd)}
.dot{top:470px;width:14px;height:14px;border-radius:50%;border:2px solid var(--white)}
.dot.active{background:#333;border-color:var(--white)}
.search-tab{left:1167px;top:165px;width:28px;height:229px;background:var(--white);border-radius:14px}
.search-tab span{position:absolute;left:4px;top:70px;writing-mode:vertical-rl;font-size:13px;color:var(--grey-text)}
.feature{top:551px;width:80px;height:80px;border-radius:50%;border:2px solid #9db8d3;background:#f4f7fa}
.profile-panel{left:0;top:713px;width:248px;height:295px;background:var(--grey)}
.avatar{border-radius:50%;background:linear-gradient(180deg,#c9b4a4,#4a4f5a)}
.profile-name{left:0;top:860px;width:248px;text-align:center;font-weight:700;font-size:15px;color:var(--link)}
.profile-row{left:40px;font-size:14px;color:var(--grey-text)}
.handle-pill{left:0;top:892px;width:198px;height:27px;border:1.5px solid var(--grey-mid);border-radius:14px}
.info-col{left:258px;top:713px;width:288px;height:295px;background:var(--grey)}
.info-row{left:258px;width:288px;height:41px;border-bottom:2px solid #f5f5f6;padding:11px 40px;font-size:14px;color:var(--grey-text)}
.project-col{left:553px;top:713px;width:647px;height:295px;background:var(--grey)}
.project-title{left:585px;top:724px;font-weight:700;font-size:15px;color:var(--link)}
.crumbs{left:585px;top:764px;font-size:14px;color:var(--grey-text)}
.payment-row{left:553px;top:796px;width:647px;height:40px;background:var(--white);padding:10px 32px;font-size:14px;font-weight:700;color:#9a9da2}
.desc-label{left:585px;top:849px;font-size:14px;color:var(--grey-text)}
.desc-text{left:585px;top:874px;width:590px;font-size:12.5px;line-height:21px;color:#b0b3b8}
.menu-item{left:0;width:243px;height:30px;border:1.5px solid var(--grey-mid);border-left:none;border-radius:0 15px 15px 0;font-size:15px;color:var(--grey-text);line-height:27px;padding-left:90px}
.menu-item.active{border-color:var(--pill-line)}
.menu-icon{position:absolute;left:22px;top:6px;width:16px;height:14px;border:1.5px solid #b9bcc1;border-radius:3px}
.menu-sep{position:absolute;left:66px;top:0;width:1.5px;height:27px;background:var(--grey-mid)}
.section-pill{left:328px;top:1054px;width:544px;height:32px;border-radius:16px;background:var(--grey);text-align:center;line-height:32px;font-weight:700;font-size:14px;color:var(--link)}
.client-head{left:319px;top:1127px;width:798px;height:30px;border:2px solid var(--pill-line);border-radius:15px;display:flex;font-size:13px;font-weight:700;color:#8b8e93}
.client-head div{text-align:center;line-height:26px}
.client-body{left:311px;top:1168px;width:816px;height:270px;background:#ecebea}
.client-row{left:321px;width:798px;height:29px;border:2px solid var(--white);border-radius:15px;display:flex;font-size:13px;color:var(--white)}
.client-row.blue{border-color:var(--pill-line)}
.client-row div{line-height:25px;text-align:center}
.c1{width:178px}.c2{width:382px}.c3{flex:1;font-weight:700}
.divider{left:0;top:1451px;width:1200px;height:2px;background:#c6d9ee}
.partner-card{left:0;top:1453px;width:258px;height:210px;background:linear-gradient(180deg,#2d6197,var(--card));box-shadow:0 3px 6px rgba(0,0,0,.25)}
.partner-name{left:0;top:1557px;width:258px;text-align:center;font-weight:700;font-size:15px;color:var(--white)}
.partner-handle{left:0;top:1590px;width:258px;text-align:center;font-size:15px;color:var(--white)}
.partner-loc{left:0;top:1620px;width:258px;height:30px;background:#6d8fb3;text-align:center;line-height:30px;font-size:15px;color:var(--white)}
.pill{height:32px;border-radius:16px;background:var(--pill);color:var(--white);font-size:14px;text-align:center;line-height:32px}
.pill.ghost{background:#eef4fb;border:1.5px solid #c9def3;color:var(--grey-text);line-height:29px}
.flag{left:970px;top:1491px;width:40px;height:40px;border-radius:50%;background:linear-gradient(135deg,#2c4a8a 40%,#d14a4a 40%,#f3f3f3 75%)}
.meta{font-size:14px;color:var(--grey-text)}
.pm-line{left:313px;top:1632px;width:804px;height:4px;background:var(--pill)}
.pm-title{left:313px;top:1643px;width:804px;text-align:center;font-weight:700;font-size:14px;color:#8b8e93}
.pm-table{left:313px;top:1665px;width:804px;background:var(--table)}
.pm-row{display:flex;height:39px;border-bottom:1px solid #c8def6;font-size:13px;color:var(--white);align-items:center}
.pm-row.head{height:38px;font-weight:700;background:#9dc5f2}
.p1{width:190px;padding-left:37px}.p2{width:466px;text-align:center}.p3{flex:1;text-align:center}
.status{display:inline-block;width:147px;height:26px;border-radius:13px;background:var(--white);color:var(--link);font-weight:700;line-height:24px;text-align:center;margin-left:10px}
.status.first{background:transparent;border:2px solid var(--white);color:var(--white)}
.create-box{left:313px;top:1950px;width:817px;height:379px;background:#f4f5f6;border:1px solid #e4e6e8}
.create-banner{left:313px;top:1964px;width:534px;height:34px}
.create-banner span{position:absolute;left:142px;top:8px;font-weight:700;font-size:14px;color:var(--grey-text)}
.label-blue{font-size:15px;color:var(--link)}
.slider-track{left:348px;top:2054px;width:440px;height:4px;background:#d5e5f6;border-radius:2px}
.slider-fill{left:348px;top:2054px;width:243px;height:4px;background:var(--pill);border-radius:2px}
.slider-knob{left:583px;top:2048px;width:16px;height:16px;border-radius:50%;background:var(--pill);border:2px solid var(--white)}
.tick{font-size:13px;color:var(--grey-text)}
.sep{left:313px;width:817px;height:1px;background:#dfe1e4}
.textarea{left:348px;top:2155px;width:769px;height:83px;border:1px solid #dfe1e4;background:#fafbfb;padding:8px 12px;font-size:13px;color:#c3c5c9}
.add-btn{left:640px;top:2281px;width:163px;height:29px;border-radius:15px;background:var(--pill);color:var(--white);font-weight:700;font-size:13px;text-align:center;line-height:29px}
</style>
</head>
<body>
<div class="canvas">
  <div class="abs top-bar"></div>
  <a class="abs nav-link" style="left:170px">Home</a>
  <a class="abs nav-link" style="left:248px">About Us</a>
  <a class="abs nav-link" style="left:344px">Contact Us</a>
  <div class="abs login">Login</div>

  <section class="abs hero"></section>
  <div class="abs logo"><span class="logo-mark"></span><span class="logo-name">Kelvrim</span></div>
  <div class="abs hero-visual" role="img" aria-label="Desktop monitor, tablet and phone showing the platform"></div>
  <svg class="abs" style="left:8px;top:258px" width="34" height="44" viewBox="0 0 34 44"><path d="M30 4 L6 22 L30 40 L24 22 Z" fill="#1e2a3a"/></svg>
  <svg class="abs" style="left:1094px;top:258px" width="34" height="44" viewBox="0 0 34 44"><path d="M4 4 L28 22 L4 40 L10 22 Z" fill="#1e2a3a"/></svg>
  <div class="abs dot active" style="left:410px"></div>
  <div class="abs dot" style="left:437px"></div>
  <div class="abs dot" style="left:465px"></div>
  <div class="abs dot" style="left:491px"></div>
  <div class="abs search-tab">
    <svg class="abs" style="left:3px;top:4px" width="22" height="22" viewBox="0 0 22 22"><circle cx="11" cy="11" r="11" fill="var(--hero)"/><circle cx="10" cy="10" r="4" fill="none" stroke="#fff" stroke-width="1.6"/><path d="M13 13 L16 16" stroke="#fff" stroke-width="1.6"/></svg>
    <span>Search here</span>
  </div>

  <div class="abs feature" style="left:210px"><svg width="80" height="80" viewBox="0 0 80 80"><path d="M24 40 L40 26 L56 40 M29 37 V54 H51 V37 M37 54 V45 H43 V54" fill="none" stroke="#9db8d3" stroke-width="2.5"/></svg></div>
  <div class="abs feature" style="left:566px"><svg width="80" height="80" viewBox="0 0 80 80"><circle cx="40" cy="40" r="16" fill="none" stroke="#9db8d3" stroke-width="2.5"/><path d="M24 40 H56 M40 24 C32 32 32 48 40 56 M40 24 C48 32 48 48 40 56" fill="none" stroke="#9db8d3" stroke-width="2"/></svg></div>
  <div class="abs feature" style="left:913px"><svg width="80" height="80" viewBox="0 0 80 80"><rect x="26" y="24" width="28" height="32" rx="4" fill="none" stroke="#9db8d3" stroke-width="2.5"/><path d="M33 32 C33 42 38 48 47 49 L47 44 L43 43 L41 45 C38 44 36 41 36 38 L38 36 L37 32 Z" fill="#9db8d3"/></svg></div>

  <div class="abs profile-panel"></div>
  <div class="abs avatar" style="left:76px;top:749px;width:100px;height:100px" role="img" aria-label="Client profile photo"></div>
  <div class="abs profile-name">LIRA VONT</div>
  <div class="abs handle-pill"></div>
  <svg class="abs" style="left:36px;top:899px" width="14" height="12" viewBox="0 0 14 12"><rect x="1" y="1" width="12" height="10" fill="none" stroke="#b9bcc1" stroke-width="1.5"/><path d="M1 1 L7 6 L13 1" fill="none" stroke="#b9bcc1" stroke-width="1.5"/></svg>
  <div class="abs profile-row" style="left:66px;top:897px">@liravont</div>
  <svg class="abs" style="left:38px;top:933px" width="12" height="16" viewBox="0 0 12 16"><path d="M6 15 C2 9 1 7 1 5 A5 5 0 0 1 11 5 C11 7 10 9 6 15 Z" fill="#b9bcc1"/><circle cx="6" cy="5" r="2" fill="#e9eaec"/></svg>
  <div class="abs profile-row" style="left:66px;top:933px">Maryland, USA</div>
  <svg class="abs" style="left:37px;top:971px" width="18" height="18" viewBox="0 0 18 18"><rect x="1" y="3" width="13" height="14" fill="none" stroke="#b9bcc1" stroke-width="1.5"/><path d="M7 11 L16 2" stroke="#b9bcc1" stroke-width="2"/></svg>
  <div class="abs profile-row" style="left:66px;top:972px">Edit Profile</div>

  <div class="abs info-col"></div>
  <div class="abs info-row" style="top:713px">Company Name: Mipsum Dolor</div>
  <div class="abs info-row" style="top:754px">Company Type: Mobil Application</div>
  <div class="abs info-row" style="top:795px">Phone : (555)-014-2290</div>
  <div class="abs info-row" style="top:836px">Email id: lira@venmaro.example</div>
  <div class="abs info-row" style="top:877px">55 Days</div>
  <div class="abs info-row" style="top:918px">20 Feb, 2016</div>
  <div class="abs info-row" style="top:959px;border:none">$ 4,50</div>

  <div class="abs project-col"></div>
  <div class="abs project-title">PROJECT TEST</div>
  <div class="abs crumbs">Home&nbsp; Working &nbsp; Project &nbsp; Project Test</div>
  <div class="abs payment-row">PAYMENT MILESTONE - PROJECT NAME</div>
  <div class="abs desc-label">Description:</div>
  <p class="abs desc-text">Proin gravida nibh vel velit auctor aliquet. Aenean sollicitudin, lorem quis bibendum auctor, nisi elit consequat ipsum, nec sagittis sem nibh id elit. Duis sed odio sit amet nibh vulputate cursus a sit amet mauris. Morbi accumsan ipsum velit. Nam nec tellus a odio tincidunt auctor a ornare odio. Sed non&nbsp; mauris vitae erat consequat auctor eu in elit. Class aptent taciti sociosqu ad litora torquent per conubia nostra, per inceptos himenaeos.</p>

  <nav>
    <div class="abs menu-item active" style="top:1046px"><i class="menu-icon"></i><i class="menu-sep"></i>Dashboard</div>
    <div class="abs menu-item" style="top:1087px"><i class="menu-icon"></i><i class="menu-sep"></i>Post Projects</div>
    <div class="abs menu-item" style="top:1128px"><i class="menu-icon"></i><i class="menu-sep"></i>All Projects</div>
    <div class="abs menu-item" style="top:1169px"><i class="menu-icon"></i><i class="menu-sep"></i>Open Projects</div>
    <div class="abs menu-item" style="top:1210px"><i class="menu-icon"></i><i class="menu-sep"></i>Closed Projects</div>
    <div class="abs menu-item" style="top:1251px"><i class="menu-icon" style="border-radius:50%"></i><i class="menu-sep"></i>Cancelled Projects</div>
    <div class="abs menu-item" style="top:1292px"><i class="menu-icon"></i><i class="menu-sep"></i>Transaction</div>
    <div class="abs menu-item" style="top:1333px"><i class="menu-icon"></i><i class="menu-sep"></i>Mail</div>
    <div class="abs menu-item" style="top:1374px"><i class="menu-icon"></i><i class="menu-sep"></i>Notification</div>
    <div class="abs menu-item" style="top:1415px"><i class="menu-icon" style="border-radius:50% 50% 2px 2px"></i><i class="menu-sep"></i>Support</div>
  </nav>

  <div class="abs section-pill">CLIENT MILESTONE</div>
  <div class="abs client-head"><div class="c1" style="border-right:1.5px solid var(--pill-line)">$ AMOUNT</div><div class="c2" style="border-right:1.5px solid var(--pill-line);color:var(--link)">$ AMOUNTDESCRIPTION</div><div class="c3">STATUS</div></div>
  <div class="abs client-body"></div>
  <div class="abs client-row" style="top:1185px"><div class="c1">$ 100.00</div><div class="c2">Lorem ipsum dolor sit amet, consectetuer</div><div class="c3">RELEASE</div></div>
  <div class="abs client-row blue" style="top:1227px"><div class="c1">$ 100.00</div><div class="c2">Lorem ipsum dolor sit amet, consectetuer</div><div class="c3">RELEASE</div></div>
  <div class="abs client-row" style="top:1269px"><div class="c1">$ 100.00</div><div class="c2">Lorem ipsum dolor sit amet, consectetuer</div><div class="c3">RELEASE</div></div>
  <div class="abs client-row blue" style="top:1311px"><div class="c1">$ 100.00</div><div class="c2">Lorem ipsum dolor sit amet, consectetuer</div><div class="c3">RELEASE</div></div>
  <div class="abs client-row" style="top:1353px"><div class="c1">$ 100.00</div><div class="c2">Lorem ipsum dolor sit amet, consectetuer</div><div class="c3">RELEASE</div></div>
  <div class="abs client-row blue" style="top:1395px"><div class="c1">$ 100.00</div><div class="c2">Lorem ipsum dolor sit amet, consectetuer</div><div class="c3">RELEASE</div></div>

  <div class="abs divider"></div>
  <div class="abs partner-card"></div>
  <div class="abs avatar" style="left:90px;top:1472px;width:76px;height:76px;border:3px solid #7ed321" role="img" aria-label="Partner profile photo"></div>
  <div class="abs partner-name">OREN PASK</div>
  <div class="abs partner-handle">@orenpask</div>
  <div class="abs partner-loc">Maryland, uSA</div>

  <div class="abs pill" style="left:346px;top:1493px;width:152px">Partner</div>
  <div class="abs pill" style="left:530px;top:1490px;width:152px">Awarded</div>
  <div class="abs pill" style="left:717px;top:1490px;width:152px">$ 4,560</div>
  <div class="abs flag" role="img" aria-label="Country flag"></div>
  <div class="abs pill ghost" style="left:523px;top:1561px;width:152px">Message</div>
  <div class="abs meta" style="left:687px;top:1568px">Last Login 40 Mins Ago</div>
  <svg class="abs" style="left:976px;top:1558px" width="28" height="28" viewBox="0 0 28 28"><rect x="2" y="6" width="20" height="20" fill="none" stroke="var(--pill)" stroke-width="2.5"/><path d="M7 15 L12 21 L26 4" fill="none" stroke="var(--pill)" stroke-width="3"/></svg>
  <div class="abs meta" style="left:1010px;top:1568px">Verified</div>

  <div class="abs pm-line"></div>
  <div class="abs pm-title">PARTNER MILESTONE</div>
  <div class="abs pm-table">
    <div class="pm-row head"><div class="p1">$ AMOUNT</div><div class="p2">DESCRIPTION</div><div class="p3">STATUS</div></div>
    <div class="pm-row"><div class="p1">$ 100.00</div><div class="p2">Lorem ipsum dolor sit amet, consectetuer</div><div class="p3"><span class="status first">RELEASED</span></div></div>
    <div class="pm-row"><div class="p1">$ 100.00</div><div class="p2">Lorem ipsum dolor sit amet, consectetuer</div><div class="p3"><span class="status">RELEASED</span></div></div>
    <div class="pm-row"><div class="p1">$ 100.00</div><div class="p2">Lorem ipsum dolor sit amet, consectetuer</div><div class="p3"><span class="status">RELEASED</span></div></div>
    <div class="pm-row"><div class="p1">$ 100.00</div><div class="p2">Lorem ipsum dolor sit amet, consectetuer</div><div class="p3"><span class="status">RELEASED</span></div></div>
    <div class="pm-row"><div class="p1">$ 100.00</div><div class="p2">Lorem ipsum dolor sit amet, consectetuer</div><div class="p3"><span class="status">RELEASED</span></div></div>
    <div class="pm-row"><div class="p1">$ 100.00</div><div class="p2">Lorem ipsum dolor sit amet, consectetuer</div><div class="p3"><span class="status">RELEASED</span></div></div>
  </div>

  <div class="abs create-box"></div>
  <div class="abs create-banner">
    <svg width="534" height="34" viewBox="0 0 534 34"><path d="M0 0 H514 L534 17 L514 34 H0 Z" fill="#dcdddf"/></svg>
    <span>CREATE A MILESTONE FOR PARTNER</span>
  </div>
  <div class="abs label-blue" style="left:348px;top:2024px"><b>$ Amount:</b> <span style="color:var(--grey-text)">Ex-90 USD</span></div>
  <div class="abs slider-track"></div>
  <div class="abs slider-fill"></div>
  <div class="abs slider-knob"></div>
  <div class="abs tick" style="left:348px;top:2064px">$0</div>
  <div class="abs tick" style="left:511px;top:2064px">$2500</div>
  <div class="abs tick" style="left:568px;top:2072px">$3300</div>
  <div class="abs tick" style="left:748px;top:2064px">$5000</div>
  <div class="abs pill" style="left:799px;top:2039px;width:315px">Amount Funded : $3300</div>
  <div class="abs sep" style="top:2112px"></div>
  <div class="abs label-blue" style="left:348px;top:2125px">Description:</div>
  <div class="abs textarea">lorem ipsum dolor sit amet, consectetuer</div>
  <div class="abs sep" style="top:2264px"></div>
  <div class="abs add-btn">ADD MILESTONE</div>
</div>
</body>
</html>
```